Menu Design Project

We are a cafe in italy our name is "Kerno Valsti Cafe & Food"

We need a new menu we offer cafes and snacks.

our web site is kernovalsti.com you can find there our logo.

We need something clean to print so we can offer to our clients a good menu.

Target Market(s)

cafe clients

Industry/Entity Type

Cafe

Requirements
Must have
• - Nice design
- Our logo
- Demo text so we can write our text

```html
<!DOCTYPE html>
<html lang="en">
<head>
<meta charset="utf-8">
<title>Kerno Valsti Cafe &amp; Food – Menu</title>
<link href="https://fonts.googleapis.com/css2?family=Roboto+Condensed:wght@300;400;700&family=Arimo:ital,wght@0,400;0,700;1,400&display=swap" rel="stylesheet">
<style>
  :root {
    --wood-dark: #141210;
    --wood-mid: #25201c;
    --wood-light: #332c26;
    --orange: #f7a12b;
    --orange-deep: #e58a14;
    --text-light: #f4f1ec;
  }
  * { margin: 0; padding: 0; box-sizing: border-box; }
  html, body { width: 728px; height: 1200px; overflow: hidden; background: var(--wood-dark); }
  .menu {
    position: relative;
    width: 728px;
    height: 1200px;
    overflow: hidden;
    font-family: "Arimo", Arial, sans-serif;
    color: var(--text-light);
  }
  .wood-texture {
    position: absolute; inset: 0;
    background:
      radial-gradient(ellipse at 30% 20%, var(--wood-light) 0%, transparent 55%),
      radial-gradient(ellipse at 75% 70%, var(--wood-mid) 0%, transparent 60%),
      linear-gradient(180deg, var(--wood-mid) 0%, var(--wood-dark) 45%, var(--wood-mid) 100%);
  }
  .brand {
    position: absolute; top: 60px; left: 0; width: 728px;
    display: flex; justify-content: center; align-items: center; gap: 12px;
  }
  .brand-dot {
    width: 34px; height: 34px; border-radius: 50%;
    border: 3px solid var(--orange);
  }
  .brand-name {
    font-family: "Roboto Condensed", Arial, sans-serif;
    font-weight: 400; font-size: 44px; color: var(--orange);
    letter-spacing: 1px;
  }
  .band {
    position: absolute; left: 0; width: 728px;
    background: linear-gradient(90deg, var(--orange-deep), var(--orange) 50%, var(--orange-deep));
  }
  .band-top { top: 180px; height: 19px; }
  .band-bottom-wide { top: 1100px; height: 22px; }
  .band-bottom-thin { top: 1126px; height: 9px; }
  .heading {
    position: absolute;
    font-family: "Roboto Condensed", Arial, sans-serif;
    font-weight: 300; color: var(--orange);
    border-bottom: 1px solid var(--orange);
    line-height: 1.1;
  }
  .heading-menu { top: 220px; left: 0; width: 728px; text-align: center; font-size: 29px; border: none; }
  .heading-menu span { border-bottom: 1px solid var(--orange); padding: 0 2px 2px; }
  .heading-brunch { font-size: 18px; }
  .brunch-left-title { top: 292px; left: 115px; }
  .brunch-right-title { top: 297px; left: 542px; }
  .heading-lunch { top: 651px; left: 0; width: 728px; text-align: center; font-size: 18px; border: none; }
  .heading-lunch span { border-bottom: 1px solid var(--orange); padding-bottom: 1px; }

  .brunch-col { position: absolute; width: 270px; list-style: none; }
  .brunch-left { left: 40px; top: 338px; }
  .brunch-right { left: 445px; top: 338px; }
  .brunch-item { margin-bottom: 18px; }
  .brunch-item.gap-after { margin-bottom: 32px; }
  .item-name {
    display: block; font-weight: 700; color: var(--orange);
    font-size: 10.5px;
  }
  .brunch-item .item-name { padding-left: 15px; margin-bottom: 1px; }
  .item-desc { font-style: italic; font-size: 10.3px; line-height: 1.3; }

  .lunch-list {
    position: absolute; top: 697px; left: 114px; width: 500px;
    list-style: none; text-align: center;
  }
  .lunch-item { margin-bottom: 10px; }
  .lunch-item .item-name { font-size: 9.5px; margin-bottom: 2px; }
  .lunch-item .item-desc { font-size: 8.4px; line-height: 1.35; }

  .contact {
    position: absolute; top: 1148px; left: 512px; width: 210px;
    font-size: 7.6px; line-height: 1.45; color: var(--orange);
  }
</style>
</head>
<body>
<main class="menu">
  <div class="wood-texture" role="img" aria-label="Dark end-grain wood block background"></div>

  <header class="brand">
    <span class="brand-dot"></span>
    <span class="brand-name">Kerno Valsti</span>
  </header>

  <div class="band band-top"></div>

  <h1 class="heading heading-menu"><span>MENU</span></h1>

  <h2 class="heading heading-brunch brunch-left-title">BRUNCH</h2>
  <ul class="brunch-col brunch-left">
    <li class="brunch-item"><span class="item-name">Steak* &amp; Eggs</span><p class="item-desc">Our petite sirloin, seasoned and perfectly cooked, combined with cheesy, scrambled eggs. Served with brunch potatoes and garnished with fresh seasonal fruit.</p></li>
    <li class="brunch-item gap-after"><span class="item-name">Omelets</span><p class="item-desc">Our light and fluffy cheese omelets are served with brunch potatoes.</p></li>
    <li class="brunch-item"><span class="item-name">Spinach &amp; Mushroom</span><p class="item-desc">Baby portabella mushrooms, Swiss cheese, artichokes, and a creamy spinach sauce.</p></li>
    <li class="brunch-item"><span class="item-name">Western</span><p class="item-desc">Green and red peppers, ham, cheese, bacon, and diced onions.</p></li>
    <li class="brunch-item"><span class="item-name">Crabacado</span><p class="item-desc">Sweet, rich jumbo lump crab meat, fresh, ripe avocado slices, Swiss cheese, and creamy Parmesan sauce.</p></li>
  </ul>

  <h2 class="heading heading-brunch brunch-right-title">BRUNCH</h2>
  <ul class="brunch-col brunch-right">
    <li class="brunch-item"><span class="item-name">Steak* &amp; Eggs</span><p class="item-desc">Our petite sirloin, seasoned and perfectly cooked, combined with cheesy, scrambled eggs. Served with brunch potatoes and garnished with fresh seasonal fruit.</p></li>
    <li class="brunch-item gap-after"><span class="item-name">Omelets</span><p class="item-desc">Our light and fluffy cheese omelets are served with brunch potatoes.</p></li>
    <li class="brunch-item"><span class="item-name">Spinach &amp; Mushroom</span><p class="item-desc">Baby portabella mushrooms, Swiss cheese, artichokes, and a creamy spinach sauce.</p></li>
    <li class="brunch-item"><span class="item-name">Western</span><p class="item-desc">Green and red peppers, ham, cheese, bacon, and diced onions.</p></li>
    <li class="brunch-item"><span class="item-name">Crabacado</span><p class="item-desc">Sweet, rich jumbo lump crab meat, fresh, ripe avocado slices, Swiss cheese, and creamy Parmesan sauce.</p></li>
  </ul>

  <h2 class="heading heading-lunch"><span>LUNCH</span></h2>
  <ul class="lunch-list">
    <li class="lunch-item"><span class="item-name">Petite Sirloin* &amp; Lobster Tail</span><p class="item-desc">Our petite sirloin paired with a sweet and tender broiled lobster tail.</p></li>
    <li class="lunch-item"><span class="item-name">Hickory Bourbon Salmon</span><p class="item-desc">A griddled salmon filet glazed with bourbon barbecue sauce.</p></li>
    <li class="lunch-item"><span class="item-name">Black Fire Sirloin* &amp; Jumbo Spicy Shrimp</span><p class="item-desc">A spicy blend of both land and sea. The Black Fire Sirloin is blackened, bold, and flavorful, while the jumbo shrimp are bursting with heat.</p></li>
    <li class="lunch-item"><span class="item-name">Blackened Tilapia with mango salsa</span><p class="item-desc">A tender filet of tilapia with Creole seasonings. Topped with handmade mango salsa with green peppers, onions, cilantro, tomatoes, and ripe mango.</p></li>
    <li class="lunch-item"><span class="item-name">New Orleans Seafood</span><p class="item-desc">Spicy, broiled tilapia topped with sautéed shrimp and rich Parmesan cream sauce.</p></li>
    <li class="lunch-item"><span class="item-name">Black Fire New York Strip*</span><p class="item-desc">A premium cut with just the right seasoning seared to juicy perfection.</p></li>
    <li class="lunch-item"><span class="item-name">Petite Sirloin* &amp; Lobster Mac 'n Cheese</span><p class="item-desc">Our petite sirloin paired with the ultimate mac 'n cheese, made with tender lobster meat.</p></li>
    <li class="lunch-item"><span class="item-name">Caribbean Chicken</span><p class="item-desc">The islands are calling with this fresh chicken breast dry rubbed with jerk seasoning and topped with mango salsa.</p></li>
    <li class="lunch-item"><span class="item-name">Shellfish Trio</span><p class="item-desc">A premium, jumbo lump crab cake, tender broiled lobster tail, and grilled jumbo shrimp brushed with garlic scampi butter.</p></li>
  </ul>

  <div class="band band-bottom-wide"></div>
  <div class="band band-bottom-thin"></div>

  <address class="contact" style="font-style: normal;">
    kerno valsti via l. ventura 12 - piva 04218830571<br>
    tel.: +39 02 55501234 - Marco + 39 333 5550187<br>
    - info@kernovalsti.com
  </address>
</main>
</body>
</html>
```